LOOP 20th Anniversary Letterhead

LOOP – Guidance, Reach, and Insight – is Harbor Works’s premiere Frontline Associate training program. LOOP includes compliance training, professional development, skill building, and training for corporate and sector-specific initiatives for all Harbor Works Frontline Associates.

We are celebrating our 20th anniversary in 2017! We would like our letterhead and logo to include some nod to this 20th anniversary. We're open to ideas that showcases this great milestone for the program. We will use this letterhead to showcase our anniversary in multiple training and marketing mediums throughout the year.

Logo: We would like to include our current logo with something to call out our 20th anniversary; we won't need a totally new logo from scratch. This logo should go at the top of the letterhead. We will need to include the Harbor Works/Onward Bright logo in the footer of the letterhead. It can be smaller though.

Letterhead: This letterhead will be used both in portrait and landscape on 8 1/2 X 11 paper. Often we use this letterhead in PowerPoint for slides, as well as in a lesson plan. We need to include enough space write a title in the header.

We are open to a watermark, but would love to see letterheads with and without it.

I have included our current template and two logos (that should be used).
Updates

Project Deadline Extended
Reason: We would like to extend the deadline for this project to allow for more submissions and/or revision to current submissions. We are most interested in designs that include something about our 20th anniversary (1997 - 2017) in either our logo, the header/footer, or in a watermark.

Target Market(s)

Frontline Associates (hourly associates), Managers

Industry/Entity Type

Communication

Logo Text

LOOP 20th Anniversary

Font styles to use
Other font styles liked:
• Calibri; Century Gothic

Colors
6b449b
000000
cbcbcb

Requirements
Must have
• - Appropriate for web and print
• - EPS, JPEG, PNG
• - Purple (from the LOOP logo), black, and gray color scheme
• - Transparent
• - Space to put a title in the header
• - No more than 1 inch from the top
• - Portrait and Landscape to use on letterhead and PowerPoint
Nice to have
• - Maybe a watermark? <-- We are open to seeing designs with and without it.
• - Should look good when printed in color or black and white
Should not have
• - No stock images, clip art
• - Overly large graphics that take up too much space in the body of the letterhead. We will need to create text here.

```html
<!DOCTYPE html>
<html lang="en">
<head>
<meta charset="utf-8">
<title>LOOP 20th Anniversary Letterhead</title>
<link href="https://fonts.googleapis.com/css2?family=Arimo:wght@400;700&display=swap" rel="stylesheet">
<style>
  :root {
    --purple: #4f2f96;
    --black: #1d1b1c;
    --gray: #cbcbcb;
    --backdrop: #e4e5e9;
    --paper: #ffffff;
    --ink: #111111;
  }
  * { box-sizing: border-box; margin: 0; padding: 0; }
  html, body { width: 1200px; height: 800px; overflow: hidden; }
  body {
    background: var(--backdrop);
    font-family: "Arimo", Arial, sans-serif;
    color: var(--ink);
    position: relative;
  }
  .letterhead {
    position: absolute;
    left: 320px; top: 38px;
    width: 560px; height: 724px;
    background: var(--paper);
    box-shadow: 0 6px 22px rgba(0,0,0,.12);
    overflow: hidden;
  }
  .side-band {
    position: absolute; left: 0; top: 96px; width: 16px; bottom: 0;
    background: linear-gradient(to bottom, var(--purple) 0 74%, var(--black) 74% 100%);
  }
  .contact {
    position: absolute; right: 56px; top: 40px;
    list-style: none; font-size: 7px; line-height: 9px;
  }
  .contact li { display: flex; align-items: center; gap: 4px; }
  .contact svg { width: 6px; height: 6px; fill: var(--purple); }
  .brand {
    position: absolute; left: 60px; top: 90px;
    display: flex; align-items: center; gap: 14px;
  }
  .brand-name {
    background: var(--purple); color: var(--paper);
    font-size: 30px; font-weight: 400; letter-spacing: 3px;
    padding: 4px 14px;
  }
  .brand-details { display: flex; flex-direction: column; gap: 4px; }
  .brand-tagline {
    font-size: 7px; letter-spacing: 1px; text-transform: uppercase; color: var(--ink);
  }
  .anniversary {
    display: flex; align-items: center; gap: 6px;
    font-size: 9px; font-weight: 700; letter-spacing: 1px; color: var(--purple);
    text-transform: uppercase;
  }
  .anniversary-dot { width: 5px; height: 5px; border-radius: 50%; background: var(--purple); }
  .letter-body {
    position: absolute; left: 60px; top: 162px; width: 440px;
    font-size: 10px; line-height: 13px;
  }
  .letter-body p { margin-bottom: 13px; }
  .recipient { margin-bottom: 4px; }
  .sign-off { position: absolute; left: 60px; top: 520px; font-size: 10px; }
  .signature { display: block; width: 60px; height: 26px; margin: 4px 0 2px 10px; background: linear-gradient(90deg, #eef0f4, #dfe2e8); }
  .signer { display: block; margin-left: 10px; font-weight: 700; }
  .footer-brands {
    position: absolute; left: 60px; bottom: 34px;
    display: flex; align-items: center; gap: 12px;
    font-size: 14px; font-weight: 700; color: var(--black);
  }
  .footer-divider { width: 1px; height: 22px; background: var(--black); }
  .footer-anniversary {
    position: absolute; right: 56px; bottom: 38px;
    font-size: 8px; letter-spacing: 1px; color: var(--purple); text-transform: uppercase;
  }
</style>
</head>
<body>
  <main class="letterhead">
    <div class="side-band"></div>

    <ul class="contact">
      <li><svg viewBox="0 0 10 10"><path d="M2 1l2 2-1 1.5c.8 1.5 1.5 2.2 3 3L7.5 6l2 2-1.5 1.5C4.5 9 1 5.5.5 2.5z"/></svg>(555) 014-2290</li>
      <li><svg viewBox="0 0 10 10"><rect x="1" y="3" width="8" height="6"/><rect x="3" y="0" width="4" height="3"/></svg>(555) 014-2291</li>
      <li><svg viewBox="0 0 10 10"><path d="M0 2h10v6H0z"/></svg>hello@loopteam.org</li>
      <li><svg viewBox="0 0 10 10"><circle cx="5" cy="5" r="4.5"/></svg>www.loopteam.org</li>
    </ul>

    <header class="brand">
      <span class="brand-name">LOOP</span>
      <div class="brand-details">
        <span class="brand-tagline">Guidance, Reach, and Insight</span>
        <span class="anniversary"><span class="anniversary-dot"></span>20 Years · 1997–2017</span>
      </div>
    </header>

    <section class="letter-body">
      <p class="recipient">Lorem Ipsum<br>Lorem Ipsum Admin</p>
      <p>Lorem Ipsum is simply dummy text of the printing and typesetting industry. Lorem Ipsum has been the industry's standard dummy text ever since the 1500s, when an unknown printer took a galley of type and scrambled it to make a type specimen book. It has survived not only five centuries, but also the leap into electronic typesetting, remaining essentially unchanged.</p>
      <p>Lorem Ipsum is simply dummy text of the printing and typesetting industry. Lorem Ipsum has been the industry's standard dummy text ever since the 1500s, when an unknown printer took a galley of type and scrambled it to make a type specimen book.</p>
      <p>It has survived not only five centuries, but also the leap into electronic typesetting, remaining essentially unchanged. Lorem Ipsum is simply dummy text of the printing and typesetting industry. Lorem Ipsum has been the industry's standard dummy text ever since the 1500s, when an unknown printer took a galley of type and scrambled</p>
      <p>Lorem Ipsum is simply dummy text of the printing and typesetting industry. Lorem Ipsum has been the industry's standard dummy text ever since the 1500s, when an unknown printer took a galley of type and scrambled it to make a type specimen book. It has survived not only five centuries, but also the leap into electronic typesetting, remaining essentially unchanged.</p>
    </section>

    <div class="sign-off">
      <span>Lorem Ipsum</span>
      <span class="signature" role="img" aria-label="Handwritten signature"></span>
      <span class="signer">Lorem Ipsum Admin</span>
    </div>

    <footer class="footer-brands">
      <span class="footer-brand">Harbor Works</span>
      <span class="footer-divider"></span>
      <span class="footer-brand">Onward Bright</span>
    </footer>
    <span class="footer-anniversary">Celebrating 20 years</span>
  </main>
</body>
</html>
```